Fire Protection Company

Hi we have a company called Brenlow Protection Services and are looking for a new design we are wanting flames as the last card was great with the whole background flames but you cant really see the services offered, phone, names etc.

We need something more upmarket and professional and only have a small budget

We need the words Brenlow Protection Services, Marcus Pelwey MSBuildA - Fire Safety Consultant, Phone No 0427316508 address : PO Box 8163 TRDC 4852 ABN 71264085319, HVRA Lic.5382410 Email marcus@brenlowgroup.example.com.au

Industry/Entity Type

Fire Safety

Font styles to use
Sans Serif

Colors
ec2027
ffc214

```html
<!DOCTYPE html>
<html lang="en">
<head>
<meta charset="utf-8">
<title>Brenlow Protection Services – Business Card</title>
<link rel="stylesheet" href="https://fonts.googleapis.com/css2?family=Jost:wght@300;400;600&display=swap">
<style>
  :root {
    --ink: #000000;
    --gold: #ffc214;
    --flame-red: #ec2027;
    --flame-orange: #f7941d;
    --rule: #cfcfcf;
  }
  * { margin: 0; padding: 0; box-sizing: border-box; }
  html, body { width: 1200px; height: 686px; overflow: hidden; background: var(--ink); }
  .card {
    position: relative;
    width: 1200px;
    height: 686px;
    background: var(--ink);
    font-family: "Jost", "Helvetica Neue", Arial, sans-serif;
    color: var(--gold);
    overflow: hidden;
  }
  .company-name {
    position: absolute;
    left: 62px;
    top: 64px;
    font-size: 38px;
    font-weight: 600;
    letter-spacing: 0.3px;
    text-transform: uppercase;
  }
  .person {
    position: absolute;
    left: 61px;
    top: 364px;
  }
  .person-name {
    font-size: 30px;
    font-weight: 400;
    line-height: 36px;
  }
  .person-role {
    font-size: 20px;
    font-weight: 300;
    line-height: 26px;
    margin-top: 2px;
  }
  .contact-list {
    position: absolute;
    left: 65px;
    top: 453px;
    list-style: none;
  }
  .contact-item {
    display: flex;
    align-items: center;
    height: 35px;
  }
  .contact-icon {
    width: 27px;
    height: 27px;
    flex: none;
  }
  .contact-text {
    margin-left: 29px;
    font-size: 26px;
    font-weight: 300;
  }
  .divider {
    position: absolute;
    left: 117px;
    top: 566px;
    width: 693px;
    height: 1px;
    background: var(--rule);
  }
  .registration {
    position: absolute;
    left: 65px;
    top: 578px;
    display: flex;
    align-items: center;
  }
  .registration .contact-text {
    font-size: 16px;
    font-weight: 400;
    margin-left: 28px;
  }
  .flame-artwork {
    position: absolute;
    left: 830px;
    top: 56px;
    width: 340px;
    height: 630px;
    border-radius: 50% 50% 0 0 / 30% 30% 0 0;
    background:
      radial-gradient(ellipse 55% 70% at 55% 85%, var(--gold) 0%, var(--flame-orange) 45%, rgba(236, 32, 39, 0.55) 75%, rgba(0, 0, 0, 0) 100%);
  }
</style>
</head>
<body>
<main class="card">
  <h1 class="company-name">Brenlow Protection Services</h1>

  <section class="person">
    <p class="person-name">Marcus Pelwey MSBuildA</p>
    <p class="person-role">Fire Safety Consultant</p>
  </section>

  <ul class="contact-list">
    <li class="contact-item">
      <svg class="contact-icon" viewBox="0 0 27 27" aria-hidden="true">
        <rect width="27" height="27" fill="var(--gold)"/>
        <path d="M4 12 Q13.5 5 23 12 L21 15 L17.5 13.5 L17.5 11.5 Q13.5 10 9.5 11.5 L9.5 13.5 L6 15 Z" fill="var(--ink)"/>
        <rect x="8" y="15.5" width="11" height="4" rx="1" fill="var(--ink)"/>
      </svg>
      <span class="contact-text">0427316508</span>
    </li>
    <li class="contact-item">
      <svg class="contact-icon" viewBox="0 0 27 27" aria-hidden="true">
        <rect width="27" height="27" fill="var(--gold)"/>
        <rect x="4.5" y="7.5" width="18" height="12" fill="none" stroke="var(--ink)" stroke-width="1.6"/>
        <path d="M4.5 7.5 L13.5 14.5 L22.5 7.5 M4.5 19.5 L11 13 M22.5 19.5 L16 13" fill="none" stroke="var(--ink)" stroke-width="1.6"/>
      </svg>
      <span class="contact-text">marcus@brenlowgroup.example.com.au</span>
    </li>
    <li class="contact-item">
      <svg class="contact-icon" viewBox="0 0 27 27" aria-hidden="true">
        <rect width="27" height="27" fill="var(--gold)"/>
        <path d="M13.5 4 C9.4 4 7 6.8 7 10.2 C7 14.8 13.5 21 13.5 21 C13.5 21 20 14.8 20 10.2 C20 6.8 17.6 4 13.5 4 Z" fill="var(--ink)"/>
        <circle cx="13.5" cy="10.3" r="2.6" fill="var(--gold)"/>
        <rect x="8" y="22" width="11" height="1.6" fill="var(--ink)"/>
      </svg>
      <span class="contact-text">PO Box 8163 TRDC 4852</span>
    </li>
  </ul>

  <div class="divider"></div>

  <div class="registration">
    <svg class="contact-icon" viewBox="0 0 27 27" aria-hidden="true">
      <rect width="27" height="27" fill="var(--gold)"/>
      <circle cx="13.5" cy="13.5" r="9" fill="var(--ink)"/>
      <circle cx="14.3" cy="8.8" r="1.4" fill="var(--gold)"/>
      <path d="M12.4 11.5 L15.4 11.5 L13.9 18 L15.2 18 L14.9 19 L11.2 19 L11.5 18 L12.6 18 L13.6 12.5 L12.2 12.5 Z" fill="var(--gold)"/>
    </svg>
    <span class="contact-text">ABN 71264085319, HVRA Lic.5382410</span>
  </div>

  <div class="flame-artwork" role="img" aria-label="Illustration of tall golden and orange flames rising from the bottom right edge"></div>
</main>
</body>
</html>
```